Willow of Meadow Uniform Label Redesign

To refine our current product label designs into one, simple, modern, crisp, general look that can be adapted to all our all Natural Skin Care and Wellness products. I am inspired by the elegant versatility of products like Lumavel Botanic Beauty or Tarn Beauty label schemes. We no longer want labels that indicate scent or ingredients. We have two primary colors that we want to maintain (#096CA3 and #DEE33F), and are willing to entertain subtle additions of others, other than black. Our labels will be printed on white or clear material. We use mainly Cosmo or Boston Round container shapes, plus flat top, smooth, round jars. Maybe a faded watermark highlight the "natural" or "beautiful" side of our products. we need to convey confidence, while remaining simple. We currently use the Advantage font. Maybe Century Gothic may work. Something similar that is easy on the eyes. Maybe vertical main text? We are willing to entertain a lot of ideas. These designs will offer ideas into our eventual Website (www.willowofmeadow-example.com) redesign.

Target Market(s)

Those who are familiar with the power of natural, plant based skin care and wellness products

Industry/Entity Type

Natural Skin Care and Wellness

Font styles to use
Sans Serif
Other font styles liked:
• Century Gothic, Advantage, or similar that is easy on the eyes

Colors
0054AA
0677BA
7BADD7
CADEEF
E8F1F8
59FF00
82FF00
B8FF75
E3FFCB
F4FFEA

Requirements
Must have
• "Clean Lines"; These colors: (#096CA3 and #DEE33F)
Nice to have
• MAYBE vertical main text or a watermark image

```html
<!DOCTYPE html>
<html lang="en">
<head>
<meta charset="utf-8">
<title>Willow of Meadow — Uniform Label System</title>
<link rel="stylesheet" href="https://fonts.googleapis.com/css2?family=Questrial&display=swap">
<style>
  :root {
    --brand-blue: #096CA3;
    --brand-navy: #0E4A7E;
    --brand-deep: #0B2F6B;
    --brand-lime: #DEE33F;
    --lime-deep: #B8BE22;
    --mist: #E8F1F8;
    --paper: #FFFFFF;
    --backdrop: #DEDEDE;
    --font-main: "Questrial", "Century Gothic", sans-serif;
  }
  * { box-sizing: border-box; margin: 0; padding: 0; }
  html, body { width: 1200px; height: 1131px; overflow: hidden; }
  body {
    background: var(--backdrop);
    font-family: var(--font-main);
    position: relative;
  }

  /* Faded backdrop wordmark, kept clear of the labels */
  .backdrop-mark {
    position: absolute;
    left: 0; right: 0; top: 62px;
    text-align: center;
    color: var(--brand-navy);
    opacity: 0.2;
  }
  .backdrop-mark__word {
    font-size: 58px;
    letter-spacing: 6px;
    line-height: 1;
  }
  .backdrop-mark__rule {
    width: 520px; height: 8px;
    margin: 22px auto 0;
    background: var(--lime-deep);
  }

  /* Label panels */
  .label {
    position: absolute;
    bottom: 70px;
    background: var(--paper);
    border-radius: 6px;
    box-shadow: 0 14px 34px rgba(0,0,0,0.18);
    overflow: hidden;
    display: flex;
    flex-direction: column;
    align-items: center;
  }
  .label--cleanser { left: 120px; width: 320px; height: 880px; }
  .label--magnesium { left: 500px; width: 260px; height: 680px; }
  .label--aloe { left: 820px; width: 260px; height: 720px; }

  .label__identity {
    display: flex; flex-direction: column; align-items: center;
    padding-top: 90px;
  }
  .label--cleanser .label__identity { padding-top: 270px; }

  .brand-name {
    color: var(--brand-blue);
    font-size: 20px;
    letter-spacing: 1px;
    white-space: nowrap;
    padding-bottom: 12px;
  }
  .label--cleanser .brand-name { font-size: 24px; }
  .brand-rule { width: 120px; height: 3px; background: var(--brand-lime); }
  .label--cleanser .brand-rule { width: 150px; }

  .tagline {
    margin-top: 16px;
    font-size: 13px;
    letter-spacing: 1px;
    color: var(--brand-blue);
    white-space: nowrap;
  }
  .label--cleanser .tagline { font-size: 15px; }

  .label__panel {
    margin-top: auto;
    width: 100%;
    padding: 20px 26px 36px;
    display: flex; flex-direction: column; align-items: center;
  }
  .label--magnesium .label__panel { background: linear-gradient(90deg, #E6EA74, var(--brand-lime) 50%, #B5BA1E); }
  .label--aloe .label__panel { background: linear-gradient(90deg, #5E9CCB, var(--brand-blue) 40%, var(--brand-deep)); }

  .panel-rule { width: 100%; height: 3px; background: var(--brand-lime); }
  .label--magnesium .panel-rule { background: var(--brand-navy); }

  .product-name {
    width: 100%;
    font-size: 34px;
    font-weight: 400;
    line-height: 1.15;
    letter-spacing: 1px;
    color: var(--brand-blue);
    padding: 16px 0 12px;
  }
  .label:not(.label--cleanser) .product-name { font-size: 28px; }
  .label--aloe .product-name { color: var(--paper); }

  .product-copy {
    margin-top: 18px;
    font-size: 11.5px;
    line-height: 1.55;
    text-align: center;
    color: var(--brand-blue);
  }
  .label:not(.label--cleanser) .product-copy { font-size: 10px; }
  .label--aloe .product-copy { color: var(--mist); }

  .volume {
    margin-top: 14px;
    font-size: 15px;
    letter-spacing: 1px;
    color: var(--brand-blue);
  }
  .label--aloe .volume { color: var(--mist); }
</style>
</head>
<body>

  <div class="backdrop-mark" aria-hidden="true">
    <div class="backdrop-mark__word">Willow of Meadow</div>
    <div class="backdrop-mark__rule"></div>
  </div>

  <section class="label label--cleanser">
    <div class="label__identity">
      <div class="brand-name">Willow of Meadow</div>
      <div class="brand-rule"></div>
    </div>
    <p class="tagline">Pure · Gentle · Botanical</p>
    <div class="label__panel">
      <div class="panel-rule"></div>
      <h2 class="product-name">Conditioning<br>Facial<br>Cleanser</h2>
      <div class="panel-rule"></div>
      <p class="product-copy">Lorem ipsum dolor sit amet, consectetur adipiscing elit. Vestibulum est enim, efficitur id nisi eu, elementum commodo magna. Ut dapibus ac velit quis consectetur. Nulla vitae turpis leo.</p>
      <p class="volume">8 fl. oz. (236 ml)</p>
    </div>
  </section>

  <section class="label label--magnesium">
    <div class="label__identity">
      <div class="brand-name">Willow of Meadow</div>
      <div class="brand-rule"></div>
    </div>
    <p class="tagline">Pure · Gentle · Botanical</p>
    <div class="label__panel">
      <div class="panel-rule"></div>
      <h2 class="product-name">Magnesium<br>Lotion</h2>
      <div class="panel-rule"></div>
      <p class="product-copy">Lorem ipsum dolor sit amet, consectetur adipiscing elit. Vestibulum est enim, efficitur id nisi eu, elementum commodo magna. Ut dapibus ac velit quis consectetur. Nulla vitae turpis leo.</p>
      <p class="volume">8 fl. oz. (236 ml)</p>
    </div>
  </section>

  <section class="label label--aloe">
    <div class="label__identity">
      <div class="brand-name">Willow of Meadow</div>
      <div class="brand-rule"></div>
    </div>
    <p class="tagline">Pure · Gentle · Botanical</p>
    <div class="label__panel">
      <div class="panel-rule"></div>
      <h2 class="product-name">Aloe &amp; Shea<br>Hydrating<br>Lotion</h2>
      <div class="panel-rule"></div>
      <p class="product-copy">Lorem ipsum dolor sit amet, consectetur adipiscing elit. Vestibulum est enim, efficitur id nisi eu, elementum commodo magna. Ut dapibus ac velit quis consectetur. Nulla vitae turpis leo.</p>
      <p class="volume">8 fl. oz. (236 ml)</p>
    </div>
  </section>

</body>
</html>
```